Market Coverage Infographic

The Halvorsen, Pritchley Group, Inc. (HPGI), headquartered in New York, NY, has been the leading independent investment bank for the global media, information, marketing and technology sectors for nearly 27 years. We are looking to freshen up a graphic that we use in our corporate brochure and our pitch decks. The current version of the graphic is attached. The graphic represents the markets that we serve (the red bubbles), as well as the underlying themes that run through all of our sectors (the 4 phrases of text surrounding the bubbles). UPDATE: Our healthcare banker just left the firm, so we need to remove the "Healthcare IT & Informatics" bubble from our graphic.
We would like to explore new ways to present this information. When we had three bubbles and one phrase surrounding the circle, it was a nice way to present the data. Now that we have FOUR bubbles and 4 phrases of text, it is a little too busy. We are not tied to the bubbles, arrows, etc. and are open to new ways of visualizing the information. UPDATE: We are looking for someone to re-visualize this infographic with only 4 sector bubbles and the 4 phrases/themes.
Although the whole graphic does not need to use blue and red, those are our standard brand colors – blue is Pantone 288C and red is Pantone 187C – and should be incorporated. Our logo does not necessarily have to be, but can be, incorporated (logo is attached).
We look forward to seeing what you come up with! The winning design will be incorporated into our marketing materials. We are very eager to choose a winner that has captured the essence of the infographic and is able to visualize in a nice, clean and professional way.
Updates
Project Deadline Extended
Reason: Our Healthcare banker left so our graphic requirements have changed - we need to remove the "Healthcare IT & Informatics" sector bubble from the design. Now we have 4 sector bubbles and 4 phrases of text/themes. Can't wait to see the revisions. Feel free to message me with any specific questions. Thank you!

```html
<!DOCTYPE html>
<html lang="en">
<head>
<meta charset="utf-8">
<title>HPGI Market Coverage</title>
<link rel="stylesheet" href="https://fonts.googleapis.com/css2?family=Chewy&family=Lora:ital,wght@0,400;1,700&display=swap">
<style>
  :root {
    --brand-blue: #0202f4;
    --hub-navy: #0d2a66;
    --hub-edge: #071a45;
    --hub-text: #c9dcc0;
    --sector-red: #ff5252;
    --bubble-red: #f0302a;
    --bubble-deep: #b81410;
    --outline: #000000;
    --label-light: #fff4f2;
  }
  html, body {
    margin: 0;
    padding: 0;
    overflow: hidden;
    background: var(--brand-blue);
  }
  .canvas {
    width: 1200px;
    height: 900px;
    position: relative;
    overflow: hidden;
    background: var(--brand-blue);
  }
  .canvas svg { display: block; }
  .connector { stroke: var(--outline); stroke-width: 2.5; }
  .hub-shape { fill: var(--hub-navy); stroke: var(--hub-edge); stroke-width: 6; }
  .hub-name {
    font-family: "Lora", serif;
    font-weight: 400;
    font-size: 27px;
    fill: var(--hub-text);
    letter-spacing: 1px;
  }
  .bubble-face { fill: url(#bubbleShade); }
  .bubble-rim { fill: none; stroke: #ffffff; stroke-opacity: .55; stroke-width: 3; }
  .bubble-label {
    font-family: "Chewy", "Arial Narrow", system-ui, sans-serif;
    font-size: 26px;
    fill: #ffffff;
    stroke: #7a0a08;
    stroke-width: 1;
    paint-order: stroke;
  }
  .sector-shape { fill: var(--sector-red); stroke: var(--outline); stroke-width: 2.5; stroke-linejoin: miter; }
  .sector-track { fill: none; stroke: var(--outline); stroke-width: 2.5; }
  .sector-label {
    font-family: "Lora", serif;
    font-style: italic;
    font-weight: 700;
    font-size: 30px;
    fill: var(--label-light);
    filter: url(#labelShadow);
  }
</style>
</head>
<body>
<main class="canvas">
<svg width="1200" height="900" viewBox="0 0 1200 900" xmlns="http://www.w3.org/2000/svg">
  <defs>
    <radialGradient id="bubbleShade" cx="40%" cy="35%" r="70%">
      <stop offset="0%" stop-color="#ff4a3c"/>
      <stop offset="70%" stop-color="var(--bubble-red)"/>
      <stop offset="100%" stop-color="var(--bubble-deep)"/>
    </radialGradient>
    <filter id="labelShadow" x="-10%" y="-20%" width="120%" height="140%">
      <feDropShadow dx="2" dy="2" stdDeviation="1.5" flood-color="#4a0000" flood-opacity=".8"/>
    </filter>
    <filter id="bubbleShadow" x="-20%" y="-20%" width="140%" height="140%">
      <feDropShadow dx="-4" dy="6" stdDeviation="3" flood-color="#ffffff" flood-opacity=".5"/>
    </filter>
    <path id="sectorPiece" d="M14,0 L258.9,-217.3 A338,338 0 0 1 292.7,169 L311.8,180 L237.5,199.3 L244.2,141 L206.5,161.3 Z"/>
    <path id="sectorTrack" d="M242.7,-176.3 A300,300 0 0 1 264.9,140.8"/>
  </defs>

  <g class="hub-links">
    <line class="connector" x1="238" y1="350" x2="290" y2="244"/>
    <line class="connector" x1="310" y1="398" x2="356" y2="378"/>
    <line class="connector" x1="318" y1="504" x2="366" y2="524"/>
    <line class="connector" x1="248" y1="558" x2="310" y2="664"/>
  </g>

  <g class="hub">
    <ellipse class="hub-shape" cx="172" cy="456" rx="160" ry="116"/>
    <text class="hub-name" text-anchor="middle">
      <tspan x="176" y="430">The Halvorsen,</tspan>
      <tspan x="176" y="464">Pritchley</tspan>
      <tspan x="176" y="498">Group, Inc.</tspan>
    </text>
  </g>

  <g class="market-bubbles">
    <g class="bubble" filter="url(#bubbleShadow)">
      <circle class="bubble-face" cx="312" cy="188" r="72"/>
      <circle class="bubble-rim" cx="312" cy="188" r="70"/>
      <g transform="rotate(6 316 188)">
        <text class="bubble-label" x="316" y="180" text-anchor="middle" textLength="70" lengthAdjust="spacingAndGlyphs">Data &amp;</text>
        <text class="bubble-label" x="316" y="210" text-anchor="middle" textLength="100" lengthAdjust="spacingAndGlyphs">Analytics</text>
      </g>
    </g>
    <g class="bubble" filter="url(#bubbleShadow)">
      <circle class="bubble-face" cx="408" cy="352" r="70"/>
      <circle class="bubble-rim" cx="408" cy="352" r="68"/>
      <g transform="rotate(4 412 352)">
        <text class="bubble-label" x="412" y="344" text-anchor="middle" textLength="84" lengthAdjust="spacingAndGlyphs">Mobile &amp;</text>
        <text class="bubble-label" x="412" y="374" text-anchor="middle" textLength="90" lengthAdjust="spacingAndGlyphs">Internet</text>
      </g>
    </g>
    <g class="bubble" filter="url(#bubbleShadow)">
      <circle class="bubble-face" cx="424" cy="544" r="70"/>
      <circle class="bubble-rim" cx="424" cy="544" r="68"/>
      <g transform="rotate(4 428 544)">
        <text class="bubble-label" x="428" y="536" text-anchor="middle" textLength="78" lengthAdjust="spacingAndGlyphs">Cloud &amp;</text>
        <text class="bubble-label" x="428" y="566" text-anchor="middle" textLength="50" lengthAdjust="spacingAndGlyphs">Saas</text>
      </g>
    </g>
    <g class="bubble" filter="url(#bubbleShadow)">
      <circle class="bubble-face" cx="346" cy="732" r="78"/>
      <circle class="bubble-rim" cx="346" cy="732" r="76"/>
      <g transform="rotate(-7 350 732)">
        <text class="bubble-label" x="350" y="724" text-anchor="middle" textLength="92" lengthAdjust="spacingAndGlyphs" style="font-size:23px">Content &amp;</text>
        <text class="bubble-label" x="350" y="752" text-anchor="middle" textLength="112" lengthAdjust="spacingAndGlyphs" style="font-size:23px">Information</text>
      </g>
    </g>
  </g>

  <g class="sector-wheel" transform="translate(836 416)">
    <g transform="rotate(230)"><use href="#sectorPiece" class="sector-shape"/><use href="#sectorTrack" class="sector-track"/></g>
    <g transform="rotate(320)"><use href="#sectorPiece" class="sector-shape"/><use href="#sectorTrack" class="sector-track"/></g>
    <g transform="rotate(50)"><use href="#sectorPiece" class="sector-shape"/><use href="#sectorTrack" class="sector-track"/></g>
    <g transform="rotate(140)"><use href="#sectorPiece" class="sector-shape"/><use href="#sectorTrack" class="sector-track"/></g>
  </g>

  <g class="sector-labels" text-anchor="middle">
    <text class="sector-label"><tspan x="712" y="290">B2B &amp; B2C</tspan><tspan x="712" y="326">Media</tspan></text>
    <text class="sector-label"><tspan x="962" y="272">Markting</tspan><tspan x="962" y="308">Services &amp;</tspan><tspan x="962" y="344">Technology</tspan></text>
    <text class="sector-label"><tspan x="962" y="490">Business</tspan><tspan x="962" y="526">Information</tspan><tspan x="962" y="562">&amp;</tspan><tspan x="962" y="598">Intelligence</tspan></text>
    <text class="sector-label"><tspan x="712" y="490">Software &amp;</tspan><tspan x="712" y="526">Tech-</tspan><tspan x="712" y="562">Enabled</tspan><tspan x="712" y="598">Services</tspan></text>
  </g>
</svg>
</main>
</body>
</html>
```